Seminar Flyer

We would like a flyer describing a seminar we will be presenting to window cleaners. The seminar topic is Glass Restoration and will include discussions on types of glass, types of glass damage and solutions. I am including the following (sample) description:
"Spend a day with The PaneMaven and learn how you can benefit from learning "Glass Restoration" and the many benefits to offering this service to your clients.
Before investing a lot of "time and money" in ANY Glass Restoration System, learn what Glass Restoration is all about and how you can turn a small investment into a very profitable business. And, this new business can be easily expanded into several other related business's.
Ready to expand your business and make some great money?
"DON'T WAIT" - Start offering your clients Glass Restoration Services.
"Glass Restoration" is one of the most profitable "Add-On" businesses for the window cleaning industry and you now have an opportunity to learn from one of the industry
leaders. Lyle Brandt will be offering a full day "hands-on" seminar on Glass Restoration.
The seminar will cover:
Glass Types
Glass Damage
Glass Coatings
Glass Distortion & Breakage
Glass Restoration Systems
Glass Restoration Procedures
Customer Expectations
Marketing and Pricing a job
Hands on demonstrations
And much much more.....
And did I mention it will cover "Glass"?
This full day seminar will be presented by Lyle Brandt and sponsored by the H.Morwick Company at their facility in Redfern Point, Nevada.
Space will be limited, so you must register to attend, but the seminar and lunch is FREE.
This all day seminar will also cover discussions on:
Hard Water Spot Removal and methods for removing.
What exactly is "Tin Etch Haze" and how to prevent or remove it easily.
Minor scratch removal (light scratches and metal marks)
Tempered Glass Defects - Waivers and precautions
Excess Scratch removal (tempered Glass scratching)
Graffiti Removal (major scratch and acid etch damage)
Additional Money Makers:
Anti-Graffiti Film Application
- An easy add on business for glass restoration businesses
Hard Water Spot Removal and Glass Sealant
- An easy add on business for window cleaning businesses
Window Frame Restoration and Treatment
- An easy add on business for window cleaning businesses"
Lyle Brandt, the President of The Brandt Company, is well known in the window cleaning industry as "PaneMaven", so we want to make sure that branding is included in the flyer.
PLEASE NOTE: The flyer will be distributed as an e-mail attachment so the flyer itself will not have any specific information regarding dates and location.
Target Market(s)
Window Cleaners; small business owners.
Industry/Entity Type
Window Cleaning

```html
<!DOCTYPE html>
<html lang="en">
<head>
<meta charset="utf-8">
<title>Glass Restoration Seminar</title>
<link rel="stylesheet" href="https://fonts.googleapis.com/css2?family=Anton&family=Archivo+Black&family=Cinzel:wght@700&family=Arimo:wght@400;700&display=swap">
<style>
:root{
  --red:#d51f1a;
  --red-dark:#a8120e;
  --ink:#111;
  --white:#fff;
  --panel:rgba(255,255,255,.84);
  --bg-light:#eeeeec;
  --bg-mid:#d4d4d2;
  --band:#0c0c0c;
}
*{margin:0;padding:0;box-sizing:border-box}
html,body{width:927px;height:1200px;overflow:hidden}
body{font-family:"Arimo",Arial,sans-serif;color:var(--ink)}
.flyer{position:relative;width:927px;height:1200px;overflow:hidden;
  background:radial-gradient(ellipse at 60% 40%,var(--bg-light) 0%,var(--bg-mid) 75%,#bdbdbb 100%)}
.title{position:absolute;left:20px;font-family:"Anton",Impact,sans-serif;font-weight:400;color:var(--white);
  text-shadow:0 0 3px #000,2px 3px 6px rgba(0,0,0,.7);line-height:1;white-space:nowrap}
.title-glass{top:-4px;font-size:126px;letter-spacing:9px}
.title-restoration{top:122px;font-size:58px;letter-spacing:2.6px}
.brand-tag{position:absolute;left:474px;top:0;width:381px;height:89px;background:var(--red);
  border:3px solid var(--red-dark);box-shadow:0 3px 8px rgba(0,0,0,.4);
  display:flex;align-items:center;justify-content:center;
  font-family:"Cinzel",serif;font-weight:700;color:var(--white);font-size:33px;letter-spacing:1px}
.panel{position:absolute;background:var(--panel);box-shadow:0 1px 4px rgba(0,0,0,.25)}
.intro{left:399px;top:109px;width:511px;height:188px;padding:14px 22px 0;font-size:14px;line-height:1.25;text-align:center}
.intro p+p{margin-top:18px}
.headline{position:absolute;left:399px;top:309px;width:511px;text-align:center;
  font-family:"Archivo Black",Arial,sans-serif;color:var(--red);font-size:25px;line-height:1.15;
  text-shadow:1px 1px 0 #300,-1px -1px 0 #300,1px -1px 0 #300,-1px 1px 0 #300}
.cta{position:absolute;left:399px;top:381px;width:511px;text-align:center;font-size:14px}
.details{left:399px;top:405px;width:511px;height:679px;padding:10px 22px 0;font-size:14px;line-height:1.22}
.details .lead{text-align:center}
.details h2{font-size:15px;font-weight:700;margin:40px 0 5px 0}
.details h2.large{font-size:16.5px;margin:14px 0 4px -4px}
.details h2.money-head{margin-top:26px}
.details ul{list-style:none}
.details .cover li{line-height:17px}
.details .extra li{line-height:17.5px}
.details .money li{margin-bottom:15px;line-height:16.5px}
.photo{position:absolute;left:48px;width:327px;border:3px solid #222;outline:6px solid #f4f4f4;
  box-shadow:0 3px 10px rgba(0,0,0,.5)}
.photo-1{top:190px;height:248px;background:linear-gradient(160deg,#8fa1a8,#5e6a6d 55%,#c9cfcf)}
.photo-2{top:459px;height:256px;background:linear-gradient(170deg,#6c7b80,#3e4549 50%,#a59a8c)}
.photo-3{top:727px;height:248px;background:linear-gradient(160deg,#b9bfc2,#545a5e 50%,#d7d9d9)}
.step{position:absolute;left:-50px;width:96px;height:96px;border-radius:50%;background:var(--band);
  color:var(--white);font-family:"Archivo Black",Arial,sans-serif;font-size:34px;
  display:flex;align-items:center;justify-content:flex-end;padding-right:24px;
  box-shadow:0 0 0 3px #fff}
.step-1{top:280px}.step-2{top:545px}.step-3{top:794px}
.notice{position:absolute;left:0;top:991px;width:389px;height:93px;background:var(--red);
  border:3px solid var(--red-dark);box-shadow:0 3px 8px rgba(0,0,0,.4);color:var(--white);
  text-align:center;padding-top:10px;font-size:16px;line-height:1.2}
.notice strong{display:block;font-family:"Archivo Black",Arial,sans-serif;font-size:23px;font-weight:400;margin-bottom:2px}
.notice b{font-weight:700}
.footer-band{position:absolute;left:0;top:1107px;width:927px;height:93px;background:var(--band);
  color:var(--white);text-align:center;font-size:22.5px;line-height:1.25;padding-top:19px}
</style>
</head>
<body>
<main class="flyer">
  <h1>
    <span class="title title-glass">GLASS</span>
    <span class="title title-restoration">RESTORATION</span>
  </h1>
  <div class="brand-tag">"PaneMaven"</div>

  <section class="panel intro">
    <p>"Spend a day with The PaneMaven and learn how you can ben-<br>efit from learning "Glass Restoration" and the many benefits to<br>offering this service to your clients.</p>
    <p>Before investing a lot of "time and money" in ANY Glass Restora-<br>tion System, learn what Glass Restoration is all about and how<br>you can turn a small investment into a very profitable business.<br>And, this new business can be easily expanded into several other<br>related business's.</p>
  </section>

  <h2 class="headline">Ready to expand your business and<br>make some great money?</h2>
  <p class="cta">DON'T WAIT" - Start offering your clients Glass Restoration Services.</p>

  <section class="panel details">
    <p class="lead">"Glass Restoration" is one of the most profitable "Add-On" businesses<br>for the window cleaning industry and you now have an opportunity to<br>learn from one of the industry</p>
    <h2>The seminar will cover:</h2>
    <ul class="cover">
      <li>Glass Types</li><li>Glass Damage</li><li>Glass Coatings</li>
      <li>Glass Distortion &amp; Breakage</li><li>Glass Restoration Systems</li>
      <li>Glass Restoration Procedures</li><li>Customer Expectations</li>
      <li>Marketing and Pricing a job</li><li>Hands on demonstrations</li>
      <li>And much much more.....</li><li>And did I mention it will cover "Glass"?</li>
    </ul>
    <h2 class="large">This all day seminar will also cover discussions on:</h2>
    <ul class="extra">
      <li>Hard Water Spot Removal and methods for removing.</li>
      <li>What exactly is "Tin Etch Haze" and how to prevent or remove it easily.</li>
      <li>Minor scratch removal (light scratches and metal marks)</li>
      <li>Tempered Glass Defects - Waivers and precautions</li>
      <li>Excess Scratch removal (tempered Glass scratching)</li>
      <li>Graffiti Removal (major scratch and acid etch damage)</li>
    </ul>
    <h2 class="large money-head">Additional Money Makers:</h2>
    <ul class="money">
      <li>Anti-Graffiti Film Application<br>- An easy add on business for glass restoration businesses</li>
      <li>Hard Water Spot Removal and Glass Sealant<br>- An easy add on business for window cleaning businesses</li>
      <li>Window Frame Restoration and Treatment<br>- An easy add on business for window cleaning businesses"</li>
    </ul>
  </section>

  <div class="photo photo-1" role="img" aria-label="Shop window covered in graffiti scratches, before restoration"></div>
  <div class="photo photo-2" role="img" aria-label="Storefront glass with large etched graffiti marks"></div>
  <div class="photo photo-3" role="img" aria-label="Clear restored storefront window after treatment"></div>
  <div class="step step-1">1</div>
  <div class="step step-2">2</div>
  <div class="step step-3">3</div>

  <aside class="notice">
    <strong>Space will be limited,</strong>
    so you must register to attend, but the<br><b>seminar and lunch is FREE.</b>
  </aside>

  <footer class="footer-band">This full day seminar will be presented by Lyle Brandt and sponsored by<br>the H.Morwick Company at their facility in Redfern Point, Nevada.</footer>
</main>
</body>
</html>
```